www.brindlecourtcounsel.com - this is the current site, the logo has been designed but everything needs to be upgraded to give it a more professional look. Use your creative talent to come up with something visually appeal and professional for this Law web-site

It Professional

```html
<!DOCTYPE html>
<html lang="en">
<head>
<meta charset="utf-8">
<title>Brindle Court Counsel</title>
<link href="https://fonts.googleapis.com/css2?family=Crimson+Pro:wght@400;600;700&display=swap" rel="stylesheet">
<style>
:root{
  --red:#cf1f3a;
  --navy:#1f2c80;
  --navy-deep:#0f1d5e;
  --ink:#222;
  --muted:#777;
  --soft:#f5f5f5;
  --line:#d8d8d8;
}
*{margin:0;padding:0;box-sizing:border-box}
html,body{width:1200px;height:3267px;overflow:hidden}
body{font-family:"Crimson Pro",Georgia,serif;color:var(--ink);background:#fff;position:relative}
a{color:inherit;text-decoration:none}

/* top bar */
.topbar{position:absolute;left:0;top:0;width:1200px;height:35px;background:var(--navy-deep);color:#fff;font-size:14px}
.topbar .contact{position:absolute;left:98px;top:9px;display:flex;gap:16px;align-items:center}
.topbar .contact span{display:flex;align-items:center;gap:6px}
.topbar .social{position:absolute;right:98px;top:6px;display:flex;gap:6px}
.dot{width:23px;height:23px;border-radius:50%;display:block}

/* header */
.header{position:absolute;top:35px;left:0;width:1200px;height:122px;background:#fff}
.brand{position:absolute;left:98px;top:42px;display:flex;align-items:center;gap:8px;white-space:nowrap}
.brand .sq{width:13px;height:13px;background:var(--red)}
.brand .name{font-size:20px;font-weight:700;color:var(--navy)}
.nav{position:absolute;left:362px;top:48px;display:flex;gap:34px;font-size:17px;color:#333;white-space:nowrap}
.nav .active{color:var(--navy);font-weight:600}
.cta{position:absolute;right:100px;top:38px;border:2px solid var(--red);color:var(--red);border-radius:22px;padding:6px 20px;font-size:17px;font-weight:600;white-space:nowrap}

/* hero */
.hero{position:absolute;top:157px;left:0;width:1200px;height:510px;background:linear-gradient(120deg,#3a2a1e 0%,#8a6a4c 35%,#c9b49a 60%,#6b5540 100%)}
.hero-panel{position:absolute;right:0;top:93px;width:568px;height:266px}
.hero-panel svg{position:absolute;inset:0}
.hero-panel h1{position:absolute;left:60px;top:46px;width:508px;text-align:center;color:#fff;font-size:36px;font-weight:700;letter-spacing:.5px;white-space:nowrap;line-height:44px}
.hero-panel p{position:absolute;left:60px;top:106px;width:508px;text-align:center;color:#fff;font-size:21px;white-space:nowrap}
.hero-panel .btn{position:absolute;left:252px;top:156px;border:2px solid #fff;border-radius:20px;color:#fff;font-size:16px;padding:5px 20px;letter-spacing:.5px;white-space:nowrap}
.dots{position:absolute;left:553px;top:460px;display:flex;gap:14px}
.dots i{width:10px;height:10px;border-radius:50%;background:#fff;display:block}
.dots i.off{background:none;border:2px solid #fff}

/* section heading */
.heading{position:absolute;display:flex;align-items:center;gap:16px;white-space:nowrap}
.heading .rule{height:1px;background:#999;width:110px}
.heading h2{font-size:38px;font-weight:700;color:#111;letter-spacing:1px}
.flag{position:absolute;width:56px;height:16px;background:linear-gradient(90deg,var(--navy) 50%,var(--red) 50%);border-radius:2px}

/* about */
.about-text{position:absolute;left:98px;top:832px;width:545px;font-size:15.5px;line-height:31.5px;color:#555}
.read-more{position:absolute;left:98px;top:1109px;height:42px;width:148px;background:var(--navy);color:#fff;font-size:16px;font-weight:600;display:flex;align-items:center}
.read-more .tag{width:48px;height:42px;background:var(--red);clip-path:polygon(0 0,100% 0,70% 100%,0 100%);display:flex;align-items:center;justify-content:center;padding-right:10px}
.read-more span.t{margin-left:10px}
.about-photo{position:absolute;left:672px;top:760px;width:428px;height:388px;background:linear-gradient(180deg,#5a2a22 0%,#7b3a2c 50%,#2b1a17 100%)}

/* services */
.services{position:absolute;left:0;top:1241px;width:1200px;height:610px;background:var(--soft);border-top:1px solid #e4e4e4;border-bottom:1px solid #e4e4e4}
.svc{position:absolute;width:330px}
.svc h3{font-size:16px;font-weight:700;color:var(--navy);letter-spacing:.5px;margin-bottom:8px}
.svc p{font-size:14px;line-height:26px;color:var(--muted)}
.svc .more{display:block;margin-top:8px;font-size:14px;color:var(--red)}
.svc.left{text-align:right}
.svc-circle{position:absolute;left:452px;top:218px;width:296px;height:296px;border-radius:50%;border:5px solid #fff;box-shadow:0 2px 8px rgba(0,0,0,.15);background:linear-gradient(135deg,#9db3d6 0%,#e9dccb 45%,#4a5f8f 100%)}

/* features */
.feature{position:absolute;top:1945px;width:497px;height:244px;color:#fff;text-align:center}
.feature.red{left:98px;background:linear-gradient(160deg,#d4263f,#b51a31)}
.feature.navy{left:603px;background:linear-gradient(160deg,#26358f,#1a266e)}
.feature h3{margin-top:36px;font-size:30px;font-weight:400;letter-spacing:1px}
.feature p{width:380px;margin:10px auto 0;font-size:16px;line-height:26px}
.feature svg{margin-top:8px}

/* contact */
.contact-sec{position:absolute;left:0;top:2280px;width:1200px;height:545px;background:linear-gradient(120deg,#1c1d22 0%,#3b3a3a 45%,#1d1c1f 100%)}
.contact-sec .heading h2{color:#fff}
.contact-sec .heading .rule{background:#ccc;width:130px}
.field{position:absolute;background:#fff;font-size:12px;color:#888;padding:9px 12px;letter-spacing:.5px}
.submit{position:absolute;left:839px;top:412px;width:143px;height:39px;border-radius:20px;background:var(--red);color:#fff;font-size:17px;font-weight:700;display:flex;align-items:center;justify-content:center;letter-spacing:.5px}

/* footer */
.footer-brand{position:absolute;left:98px;top:2930px;display:flex;align-items:center;gap:8px;white-space:nowrap}
.footer-brand .sq{width:13px;height:13px;background:var(--red)}
.footer-brand .name{font-size:20px;font-weight:700;color:var(--navy)}
.f-contact{position:absolute;left:98px;font-size:14px;color:#555;display:flex;align-items:center;gap:12px;white-space:nowrap}
.f-contact .ic{width:36px;height:36px;border-radius:50%;border:1px solid #ddd;display:flex;align-items:center;justify-content:center}
.vline{position:absolute;top:2935px;width:1px;height:88px;background:var(--line)}
.fcol{position:absolute;top:2902px}
.fcol h4{font-size:17px;font-weight:700;letter-spacing:1px;color:#222;margin-bottom:12px}
.fcol ul{list-style:none;font-size:14px;color:#666;line-height:30.5px;white-space:nowrap}
.f-social{display:flex;gap:8px;margin-top:4px}
.f-social .dot{width:34px;height:34px}
.map-btn{margin-top:18px;width:146px;height:42px;background:var(--navy);color:#fff;display:flex;align-items:center;font-size:16px;font-weight:600}
.map-btn .tag{width:46px;height:42px;background:var(--red);clip-path:polygon(0 0,100% 0,72% 100%,0 100%);display:flex;align-items:center;justify-content:center;padding-right:8px}
.map-btn span.t{margin-left:12px}
.divider{position:absolute;left:98px;top:3186px;width:1002px;height:1px;background:var(--line)}
.copy{position:absolute;left:0;top:3218px;width:1200px;text-align:center;font-size:14px;color:#444}
</style>
</head>
<body>

<div class="topbar">
  <div class="contact">
    <span><svg width="14" height="11" viewBox="0 0 14 11"><rect x=".5" y=".5" width="13" height="10" fill="none" stroke="#fff"/><path d="M1 1l6 5 6-5" fill="none" stroke="#fff"/></svg>hello@brindlecourtcounsel.com</span>
    <span>|</span>
    <span><svg width="12" height="12" viewBox="0 0 24 24"><path fill="#fff" d="M6.6 10.8a15 15 0 006.6 6.6l2.2-2.2c.3-.3.7-.4 1-.2 1.1.4 2.3.6 3.6.6.6 0 1 .4 1 1V20c0 .6-.4 1-1 1A17 17 0 013 4c0-.6.4-1 1-1h3.5c.6 0 1 .4 1 1 0 1.3.2 2.5.6 3.6.1.3 0 .7-.2 1z"/></svg>+1 555-014-2290</span>
  </div>
  <div class="social">
    <i class="dot" style="background:#3b5998"></i>
    <i class="dot" style="background:#1da1f2"></i>
    <i class="dot" style="background:#e62117"></i>
    <i class="dot" style="background:#0e76a8"></i>
    <i class="dot" style="background:#dd4b39"></i>
  </div>
</div>

<header class="header">
  <div class="brand"><i class="sq"></i><span class="name">Brindle Court Counsel</span></div>
  <nav class="nav">
    <a class="active">Home</a><a>About</a><a>Services</a><a>Estate Planning</a><a>News</a><a>Contact</a>
  </nav>
  <a class="cta">Free Consultation</a>
</header>

<section class="hero" role="img" aria-label="Lawyer reviewing documents at a desk with binders">
  <div class="hero-panel">
    <svg width="568" height="266" viewBox="0 0 568 266"><polygon points="60,0 568,0 568,266 0,266" fill="#cf1f3a" fill-opacity=".92"/></svg>
    <h1>BRINDLE COURT COUNSEL</h1>
    <p>Sed erspiciatis unde om istsit voluptatem</p>
    <a class="btn">READ MORE</a>
  </div>
  <div class="dots"><i></i><i></i><i></i><i class="off"></i></div>
</section>

<section class="about">
  <div class="flag" style="left:290px;top:756px" role="img" aria-label="Small flag ornament"></div>
  <div class="heading" style="left:100px;top:770px"><span class="rule"></span><h2>ABOUT US</h2><span class="rule"></span></div>
  <p class="about-text">I came to the United States in 2005 and I was thrown into a world of chaos, learning how to deal with issues such as immigration, taxes, and housing. As I spent more time in the states, it became clear that the US is very complicated for expats with the myriad of rules and regulations that an expat has to navigate.<br>It is my belief that by passing on my knowledge and experience, I can help expats and international investors, be better prepared and have the support they need, to successfully navigate the system. That is why my entire focus is on expats and international clients. I have a variety of resources..</p>
  <a class="read-more"><span class="tag"><svg width="16" height="14" viewBox="0 0 16 14"><path d="M1 1l6 6-6 6M8 1l6 6-6 6" fill="none" stroke="#fff" stroke-width="2"/></svg></span><span class="t">Read More</span></a>
  <div class="about-photo" role="img" aria-label="Attorney standing in front of a bookshelf of law books"></div>
</section>

<section class="services">
  <div class="flag" style="left:572px;top:105px" role="img" aria-label="Small flag ornament"></div>
  <div class="heading" style="left:382px;top:118px"><span class="rule"></span><h2>SERVICES</h2><span class="rule"></span></div>

  <div class="svc left" style="left:97px;top:220px">
    <h3>SPECIAL NEEDS PLANNING</h3>
    <p>If you currently support or provide care for a child or loved one with special needs (such as physical and/or mental disabilities), what would you do if</p>
    <a class="more">Read More »</a>
  </div>
  <div class="svc left" style="left:97px;top:392px">
    <h3>REAL ESTATE SERVICES</h3>
    <p>It can be quite difficult for expats to avoid all real estate risk when dealing with an unfamiliar market. I strive to provide my clients with all they may need to</p>
    <a class="more">Read More »</a>
  </div>
  <div class="svc-circle" role="img" aria-label="Hand signing a legal document with a pen"></div>
  <div class="svc" style="left:773px;top:220px">
    <h3>ESTATE PLANNING</h3>
    <p>While no one enjoys thinking about death or disability, establishing an estate plan is one of the most important steps you can take to protect yourself..</p>
    <a class="more">Read More »</a>
  </div>
  <div class="svc" style="left:773px;top:392px">
    <h3>LONG-TERM CARE &amp; MEDICAID</h3>
    <p>The high cost of long-term care has made planning a critically important issue for most middle-class seniors and their families. Most seniors ..</p>
    <a class="more">Read More »</a>
  </div>
</section>

<div class="feature red" role="img" aria-label="Gavel and documents tinted red">
  <h3>ESTATE TAX</h3>
  <p>Consider your US Estate Tax and Probate Avoidance and the Impact of the Estate Tax in the Foreign Country of Your Residence</p>
  <svg width="22" height="20" viewBox="0 0 22 20"><path d="M2 2l9 7 9-7M2 10l9 7 9-7" fill="none" stroke="#fff" stroke-width="2"/></svg>
</div>
<div class="feature navy" role="img" aria-label="Pen resting on a contract tinted blue">
  <h3>POWER OF ATTORNEY</h3>
  <p>Many people form a power of attorney specifically for addressing medical concerns. If a person were to become incapacitated for medical reasons</p>
  <svg width="22" height="20" viewBox="0 0 22 20"><path d="M2 2l9 7 9-7M2 10l9 7 9-7" fill="none" stroke="#fff" stroke-width="2"/></svg>
</div>

<section class="contact-sec" role="img" aria-label="Business handshake over a desk, darkened">
  <div class="flag" style="left:572px;top:96px;opacity:.7" role="img" aria-label="Small flag ornament"></div>
  <div class="heading" style="left:320px;top:110px"><span class="rule"></span><h2>CONTACT FORM</h2><span class="rule"></span></div>
  <div class="field" style="left:218px;top:201px;width:372px;height:35px">FIRST NAME</div>
  <div class="field" style="left:608px;top:201px;width:374px;height:35px">LAST NAME</div>
  <div class="field" style="left:218px;top:249px;width:372px;height:35px">PHONE</div>
  <div class="field" style="left:608px;top:249px;width:374px;height:35px">EMAIL</div>
  <div class="field" style="left:218px;top:297px;width:764px;height:96px">MESSAGE</div>
  <a class="submit">SUBMIT</a>
</section>

<footer>
  <div class="footer-brand"><i class="sq"></i><span class="name">Brindle Court Counsel</span></div>
  <div class="f-contact" style="top:3038px"><span class="ic"><svg width="14" height="11" viewBox="0 0 14 11"><rect width="14" height="11" fill="#cf1f3a"/><path d="M1 1l6 5 6-5" fill="none" stroke="#fff"/></svg></span>hello@brindlecourtcounsel.com</div>
  <div class="f-contact" style="top:3089px"><span class="ic"><svg width="14" height="14" viewBox="0 0 24 24"><path fill="#cf1f3a" d="M6.6 10.8a15 15 0 006.6 6.6l2.2-2.2c.3-.3.7-.4 1-.2 1.1.4 2.3.6 3.6.6.6 0 1 .4 1 1V20c0 .6-.4 1-1 1A17 17 0 013 4c0-.6.4-1 1-1h3.5c.6 0 1 .4 1 1 0 1.3.2 2.5.6 3.6.1.3 0 .7-.2 1z"/></svg></span>Ph : +1 555-014-2290</div>

  <span class="vline" style="left:354px"></span>
  <span class="vline" style="left:580px"></span>
  <span class="vline" style="left:840px"></span>

  <div class="fcol" style="left:405px">
    <h4>QUICK LINKS</h4>
    <ul><li>Home</li><li>About</li><li>Services</li><li>Estate Planning</li><li>News</li><li>Contact</li></ul>
  </div>
  <div class="fcol" style="left:643px">
    <h4>OTHER LINKS</h4>
    <ul><li>Sitemap</li><li>Terms and conditions</li><li>Privacy policy</li><li>Information</li><li>Brindle Legal Services</li></ul>
  </div>
  <div class="fcol" style="left:897px">
    <h4>FOLLOW US</h4>
    <div class="f-social">
      <i class="dot" style="background:#3b5998"></i>
      <i class="dot" style="background:#1da1f2"></i>
      <i class="dot" style="background:#e62117"></i>
      <i class="dot" style="background:#0e76a8"></i>
      <i class="dot" style="background:#dd4b39"></i>
    </div>
    <a class="map-btn"><span class="tag"><svg width="14" height="20" viewBox="0 0 14 20"><path d="M7 0a7 7 0 00-7 7c0 5 7 13 7 13s7-8 7-13a7 7 0 00-7-7zm0 10a3 3 0 110-6 3 3 0 010 6z" fill="#fff"/></svg></span><span class="t">View Map</span></a>
  </div>

  <div class="divider"></div>
  <p class="copy">© Copyright 2018 Brindle Court Counsel.All Rights Reserved</p>
</footer>

</body>
</html>
```